Custom Framing Shop Tallpine Framing Studio

I want an eye catching graphic that will be used a s business sign on a busy road. The sign MUST communicate the type of business it is clearly to vehicles traveling at 40 mph. This is a custom picture framing business and the sign will be hanging and be approximately 32" X 48". The business name is Tallpine Framing Studio; Custom framing: by appointment and should include a whole or partial image of a picture frame as a visual que. I've included inspiration idea's, color pallets and styles that I like and a current business card for inspiration. I like the crimson font style shadowing and background colors of the attached Olans pizzeria sign. I'd prefer crimson letters. Custom Framing is the message to communicate, followed by phone number and business name. I like the idea of a shield shape with a banner since it would more eye catching, Once again the Tallpine image and name is less important than communicating what the business does. I like Crimson, grey, gold, black but am open to new ideas . I like the idea of a shield with a banner more than a rectangle, but am open to idea's

Target Market(s)

My target market is local homeowners ($700k+) who want a relationship with their framer and are willing to pay for a customized experience compared to a craft store experience. I have more female clients then men.

Industry/Entity Type

Picture Framing Art

Other font styles liked:
• Look at the attached image of a custom pizzeria sign, its kid of a custom car pinstripe font style. Script and decorative may be difficult to read while driving by but add to the elegance.

Colors

Designer to choose colors to be used in the design.

Requirements
Must have
• Clearly communicate what the business does "Custom framing" preferably with a picture frame and words
Nice to have
• incorporate a Tallpine into the graphic
Should not have
• A Tallpine image doesn't communicate what the business does to a vehicle traveling at 40 mph by the sign

```html
<!DOCTYPE html>
<html lang="en">
<head>
<meta charset="utf-8">
<title>Tallpine Framing Studio – Custom Framing Sign</title>
<link href="https://fonts.googleapis.com/css2?family=Rye&family=Josefin+Sans:wght@600;700&display=swap" rel="stylesheet">
<style>
  :root {
    --crimson: #7a0a12;
    --crimson-deep: #5e070d;
    --gold: #d6a55a;
    --gold-dark: #9a6a2a;
    --cream: #f5e6c8;
    --cream-light: #fbf1de;
    --cream-edge: #e7cfa6;
    --ink: #1c1b18;
    --charcoal: #2b2b2b;
    --bg-light: #f4f4f4;
    --bg-dark: #d7d8d8;
  }
  html, body {
    margin: 0;
    padding: 0;
    width: 1200px;
    height: 908px;
    overflow: hidden;
  }
  body {
    background: radial-gradient(ellipse at 50% 45%, var(--bg-light) 0%, #e8e9e9 55%, var(--bg-dark) 100%);
  }
  .sign {
    display: block;
    width: 1200px;
    height: 908px;
  }
  .headline {
    font-family: "Rye", serif;
    fill: var(--crimson);
    stroke: var(--cream-light);
    stroke-width: 3;
    paint-order: stroke fill;
  }
  .banner-text {
    font-family: "Josefin Sans", sans-serif;
    font-weight: 700;
    fill: var(--cream);
    letter-spacing: 1px;
  }
  .phone {
    font-family: "Josefin Sans", sans-serif;
    font-weight: 600;
    fill: var(--cream);
  }
  .studio-name {
    font-family: "Josefin Sans", sans-serif;
    font-weight: 700;
    fill: var(--charcoal);
  }
</style>
</head>
<body>
<svg class="sign" viewBox="0 0 1200 908" xmlns="http://www.w3.org/2000/svg">
  <defs>
    <radialGradient id="panel-fill" cx="0.5" cy="0.55" r="0.6">
      <stop offset="0" stop-color="var(--cream-light)"/>
      <stop offset="1" stop-color="var(--cream-edge)"/>
    </radialGradient>
    <linearGradient id="frame-gold" x1="0" y1="0" x2="1" y2="1">
      <stop offset="0" stop-color="#7d5020" stop-opacity="0.6"/>
      <stop offset="0.25" stop-color="#c9913f"/>
      <stop offset="0.55" stop-color="#e8c074"/>
      <stop offset="0.8" stop-color="#a8732f"/>
      <stop offset="1" stop-color="#d9ae62"/>
    </linearGradient>
    <filter id="sign-shadow" x="-10%" y="-10%" width="120%" height="130%">
      <feDropShadow dx="0" dy="14" stdDeviation="14" flood-color="#000" flood-opacity="0.35"/>
    </filter>
    <filter id="frame-shadow" x="-10%" y="-10%" width="130%" height="130%">
      <feDropShadow dx="6" dy="6" stdDeviation="5" flood-color="#5a3a14" flood-opacity="0.4"/>
    </filter>
    <filter id="text-shadow" x="-5%" y="-10%" width="110%" height="130%">
      <feDropShadow dx="3" dy="6" stdDeviation="4" flood-color="#3a2a14" flood-opacity="0.55"/>
    </filter>
    <clipPath id="panel-clip">
      <polygon points="613,206 972,279 956,591 613,671 271,591 253,279"/>
    </clipPath>
  </defs>

  <!-- Shield -->
  <g class="shield" filter="url(#sign-shadow)">
    <path d="M613,187 L980,262 Q992,266 991,280 L973,598 Q972,606 962,609 L613,690 L264,609 Q254,606 253,598 L233,280 Q232,266 245,262 Z" fill="var(--ink)"/>
    <polygon points="613,195 980,271 964,600 613,680 262,600 245,271" fill="var(--gold)"/>
    <polygon points="613,198 976,273 960,597 613,677 266,597 249,273" fill="var(--crimson)"/>
    <polygon points="613,203 974,277 958,593 613,673 269,593 251,277" fill="var(--gold)"/>
    <polygon points="613,206 972,279 956,591 613,671 271,591 253,279" fill="url(#panel-fill)"/>
    <rect x="240" y="565" width="740" height="130" fill="var(--ink)" clip-path="url(#panel-clip)"/>
  </g>

  <!-- Picture frame corner -->
  <g class="frame-image" role="img" aria-label="Ornate gilded picture frame corner" filter="url(#frame-shadow)" clip-path="url(#panel-clip)">
    <polygon points="612,216 922,284 840,510 804,510 858,318 672,264 612,258" fill="url(#frame-gold)"/>
    <polyline points="612,258 672,264 858,318 804,510" fill="none" stroke="#6e4518" stroke-width="3" opacity="0.7"/>
    <polyline points="622,236 896,298 826,510" fill="none" stroke="#f3d48e" stroke-width="2" opacity="0.6"/>
  </g>

  <!-- Left ornament -->
  <rect role="img" aria-label="Crimson scroll flourish" x="268" y="292" width="110" height="30" rx="15" fill="var(--crimson)" opacity="0.18"/>

  <!-- Studio name -->
  <rect x="421" y="303" width="20" height="20" fill="var(--crimson)"/>
  <text class="studio-name" x="452" y="325" font-size="34" letter-spacing="2">TALLPINE</text>
  <text class="studio-name" x="553" y="354" font-size="15" letter-spacing="1.5">Framing Studio</text>

  <!-- Headline -->
  <text class="headline" x="284" y="486" font-size="118" textLength="658" lengthAdjust="spacingAndGlyphs" filter="url(#text-shadow)">CUSTOM FRAMING</text>

  <!-- Banner -->
  <g class="banner">
    <polygon points="203,537 320,532 335,595 226,598 258,568" fill="var(--crimson-deep)" stroke="var(--gold)" stroke-width="2.5"/>
    <polygon points="1002,537 885,532 870,595 980,598 948,568" fill="var(--crimson-deep)" stroke="var(--gold)" stroke-width="2.5"/>
    <polygon points="320,560 335,595 350,574" fill="#3e0408"/>
    <polygon points="885,560 870,595 855,574" fill="#3e0408"/>
    <path d="M298,516 Q613,488 908,514 L892,580 Q613,560 316,584 Z" fill="var(--crimson)" stroke="var(--gold)" stroke-width="2.5"/>
    <line x1="338" y1="541" x2="370" y2="540" stroke="var(--cream)" stroke-width="3"/>
    <line x1="832" y1="540" x2="864" y2="541" stroke="var(--cream)" stroke-width="3"/>
    <text class="banner-text" x="604" y="553" font-size="37" text-anchor="middle">BY APPOINTMENT</text>
  </g>

  <!-- Divider -->
  <line x1="505" y1="580" x2="720" y2="580" stroke="var(--gold)" stroke-width="1.2" opacity="0.8"/>
  <rect role="img" aria-label="Gold scroll divider ornament" x="556" y="574" width="110" height="12" rx="6" fill="var(--gold)" opacity="0.55"/>

  <!-- Phone -->
  <text class="phone" x="610" y="626" font-size="40" text-anchor="middle" letter-spacing="1">(555) 014-2760</text>
</svg>
</body>
</html>
```